Business Cards for Retail/Sourcing Business.

We need a business cards for our company where it looks like:
TK
LV

VERTICAL, where the TK is over the LV. Then Under the TKLV would be name, address and website address. We want the P to be in the style of our original logo, which I uploaded.

Also, can we get a couple of designs with fun colors - especially for the letter head.

Target Market(s)

Old clients. Many of our clients or people we do business with are 40-50 plus. We are not an industry with many young people.

Industry/Entity Type

Business

Contact Information for Business Card

Front side is just says TKLV with name, title, address, and website below.

Font styles to use
Serif
Sans Serif
Decorative
Script

Requirements
Must have
• THE TKLV design with the P in the design of the logo
Nice to have
• Fun colors, new takes on the TKLV and any other additions that would be cool and make it pop

```html
<!DOCTYPE html>
<html lang="en">
<head>
<meta charset="utf-8">
<title>TKLV Business Card and Letterhead</title>
<link href="https://fonts.googleapis.com/css2?family=Exo+2:wght@400;600&display=swap" rel="stylesheet">
<style>
  :root {
    --orange: #df8129;
    --ink: #1a1a1a;
    --paper: #ffffff;
    --ghost: #e6e5e5;
    --backdrop: #d4d4d4;
    --light-text: #ffffff;
  }
  * { margin: 0; padding: 0; box-sizing: border-box; }
  html, body {
    width: 1200px; height: 900px; overflow: hidden;
    background: var(--backdrop);
    font-family: "Exo 2", sans-serif;
  }
  .canvas { position: relative; width: 1200px; height: 900px; }

  /* Business card */
  .business-card {
    position: absolute; left: 83px; top: 266px;
    width: 337px; height: 576px;
    background: var(--paper);
    overflow: hidden;
  }
  .card-wordmark {
    position: absolute; left: 0; top: 40px; width: 100%;
    text-align: center;
    color: var(--orange);
    font-weight: 600;
    font-size: 128px;
    line-height: 118px;
    letter-spacing: 2px;
  }
  .card-band {
    position: absolute; left: 0; top: 304px; width: 100%; height: 15px;
    background: var(--orange);
  }
  .card-details {
    position: absolute; left: 0; top: 319px; width: 100%; height: 257px;
    background: var(--ink);
    color: var(--light-text);
    text-align: center;
    font-weight: 400;
    padding-top: 24px;
  }
  .card-name { color: var(--orange); font-size: 30px; line-height: 34px; letter-spacing: 1px; }
  .card-title { font-size: 20px; line-height: 26px; letter-spacing: 1px; }
  .card-phone { font-size: 27px; line-height: 32px; margin-top: 28px; letter-spacing: 1px; font-weight: 600; }
  .card-line { font-size: 20px; line-height: 27px; letter-spacing: 1px; }

  /* Letterhead */
  .letterhead {
    position: absolute; left: 490px; top: 17px;
    width: 638px; height: 825px;
    background: var(--paper);
    overflow: hidden;
  }
  .letterhead-wordmark {
    position: absolute; left: 18px; top: 14px;
    color: var(--orange);
    font-weight: 600;
    font-size: 96px;
    line-height: 88px;
    letter-spacing: 2px;
  }
  .letterhead-watermark {
    position: absolute; left: 165px; top: 350px;
    color: var(--ghost);
    font-weight: 600;
    font-size: 290px;
    line-height: 240px;
    letter-spacing: 6px;
    white-space: nowrap;
  }
  .letterhead-contact {
    position: absolute; left: 22px; right: 28px; top: 762px;
    display: flex; justify-content: space-between;
    font-size: 14px; letter-spacing: 1px;
    color: var(--ink);
    font-weight: 600;
  }
  .letterhead-contact .address { margin-left: 60px; }
  .letterhead-band {
    position: absolute; left: 0; top: 786px; width: 100%; height: 7px;
    background: var(--orange);
  }
  .letterhead-foot {
    position: absolute; left: 0; top: 793px; width: 100%; height: 32px;
    background: var(--ink);
  }
</style>
</head>
<body>
<main class="canvas">
  <section class="business-card" aria-label="Business card">
    <div class="card-wordmark">TK<br>LV</div>
    <div class="card-band"></div>
    <div class="card-details">
      <p class="card-name">Marlo Quintane</p>
      <p class="card-title">home Sourcing</p>
      <p class="card-phone">0412557830</p>
      <p class="card-line">14 east 3rd street</p>
      <p class="card-line">LV,NV</p>
      <p class="card-line">www.tekalov.com</p>
    </div>
  </section>

  <section class="letterhead" aria-label="Letterhead">
    <div class="letterhead-watermark" aria-hidden="true">TK<br>LV</div>
    <div class="letterhead-wordmark">TK<br>LV</div>
    <div class="letterhead-contact">
      <span class="phone">0412557830</span>
      <span class="address">14 east 3rd street LV,NV</span>
      <span class="web">www.tekalov.com</span>
    </div>
    <div class="letterhead-band"></div>
    <div class="letterhead-foot"></div>
  </section>
</main>
</body>
</html>
```